Guaranteed web refresh merrowquay.net.au

Collective strata website refresh merrowquay.net.au

Description:
This website is managed by the leadership of a group of buildings in Pyrmont. The area and the collective stratas are known as Merrow Quay. The current website is messy and very dated. For the new site, we'd like to focus on a clean, user friendly design. The majority of the content on this site will be text. Most pages will use a one-pager scrolling format.

Current Site:
The current site is merrowquay.net.au

This site is functionally very good, but has certain issues due to its age. We are generally quite happy with the functionality of the site, despite layout issues.

Users:

The users are those who currently live or are interested in living in Merrow quay. This group has a large demographic spread, notably including a large amount of older people. When designing remember people who may be less familiar with technology and the internet will make up many of the users of the site. 

Design:
This site should give a clean, professional and welcoming energy. It should be clean, simple and focused on efficiently displaying information to the user in an accessible and clear way.
As users typically come to the site looking for a specific piece of information or to use a service

We would like a navigation menu with the categories "Home, Services, Facilities, Stratas, About Us, Local Information, Contact”

For us to choose a winner, we would like you to design the home page, but the winner will be required to provide an example strata page (a page with some headings that link to articles below) and a standard page. They will also be required to provide all images used without charge.

If you are going to submit multiple designs or respond to feedback, please modify the menu and text layout between them. This is the most important part of the design, and multiple submissions with only minor aesthetic changes will be largely disregarded.

Requested:
Home Page

Winner to provide:
Strata Page
Standard page template

There are some photos you can use here:

https://www.lorvex.net/temp/merrowquay.zip

It contains:
A couple of the boss's own photos
Some photos from a PDF pamphlet done by a large organisation you can use
The current logos

The boss has taken a couple of photos [sigh] so if there is a way in using them somewhere on the site please do. They are not critical to use.
You do not have to use any of the photos, and if you use others remember you must provide them free with the design.

Designs look the same

```html
<!DOCTYPE html>
<html lang="en">
<head>
<meta charset="utf-8">
<title>Merrow Quay – Home</title>
<link rel="stylesheet" href="https://fonts.googleapis.com/css2?family=Lato:wght@300;400;700;900&display=swap">
<style>
:root{
  --blue:#1f5a96;
  --blue-deep:#1b4f86;
  --green:#3aa535;
  --header:#3b3b3b;
  --text:#555;
  --footer:#ececec;
  --band:linear-gradient(90deg,#1d5f8e 0%,#2d8a6a 30%,#3aa648 50%,#2d8a6a 70%,#1d5f8e 100%);
}
*{box-sizing:border-box;margin:0;padding:0}
html,body{width:1200px;height:4173px;overflow:hidden}
body{font-family:'Lato',sans-serif;color:var(--text);background:#fff;position:relative}
a{text-decoration:none;color:inherit}

.site-header{height:65px;background:var(--header);display:flex;align-items:center;position:relative}
.brand{width:275px;height:65px;display:flex;align-items:center;gap:10px;padding-left:14px}
.brand-mark{width:14px;height:14px;background:var(--green);display:block}
.brand-name{color:#fff;font-size:24px;font-weight:400;letter-spacing:.5px}
.main-nav{display:flex;gap:19px;margin-left:57px;font-size:12.5px;color:#fff;letter-spacing:.5px}
.main-nav a{padding:3px 0}
.main-nav a.active{background:var(--green);border-radius:10px;padding:3px 8px;font-weight:700}
.search{position:absolute;left:975px;top:24px;width:131px;height:20px;background:#fff;border-radius:10px;font-size:11px;color:#333;display:flex;align-items:center;justify-content:center;letter-spacing:.5px}
.search-icon{position:absolute;left:1133px;top:21px}

.hero{height:583px;background:linear-gradient(180deg,#3c5a8c 0%,#8c7aa3 40%,#d79a6e 70%,#35503a 100%)}
.hero-stripe{height:7px;background:linear-gradient(90deg,var(--green),#2a7fb1)}

main{padding:49px 70px 0}
.band{height:60px;border-radius:16px;background:var(--band);color:#fff;font-size:44px;font-weight:700;text-align:center;line-height:60px;letter-spacing:.5px}
.intro{margin:31px 10px 37px;font-size:14px;line-height:20px;text-align:center;font-weight:300;color:#444}

.grid{display:grid;grid-template-columns:484px 484px;column-gap:92px;margin-top:40px}
.services{grid-template-rows:548px 548px 500px;margin-bottom:35px}
.facilities{grid-template-rows:557px 557px;margin-top:50px}

.card{display:flex;flex-direction:column;align-items:center;text-align:center}
.photo{width:484px;height:286px;border-radius:28px;padding:3px;background:linear-gradient(180deg,#2464a2,#3aa535)}
.photo span{display:block;width:100%;height:100%;border-radius:25px}
.card h3{margin-top:20px;font-size:32px;font-weight:400;color:var(--blue);letter-spacing:.3px;text-transform:uppercase;white-space:nowrap}
.card p{margin-top:8px;font-size:14px;line-height:20px;font-weight:300;color:#444;padding:0 6px}
.btn{margin-top:16px;background:var(--green);color:#fff;font-size:14px;font-weight:700;letter-spacing:.5px;border-radius:10px;padding:4px 22px}

.site-footer{position:absolute;top:3846px;left:0;width:1200px;height:259px;background:var(--footer)}
.footer-brand{position:absolute;left:146px;top:40px;display:flex;align-items:center;gap:12px}
.footer-brand .brand-mark{width:18px;height:18px;background:var(--blue-deep)}
.footer-brand .brand-name{color:var(--blue-deep);font-size:32px}
.social{position:absolute;left:146px;top:184px;display:flex;align-items:center;gap:8px;font-size:16px;font-weight:700;color:var(--blue-deep)}
.social i{width:46px;height:46px;background:var(--blue-deep);display:block}
.footer-col{position:absolute;top:38px;font-size:14px;line-height:20px;color:#666}
.footer-col h4{color:var(--blue);font-size:15px;font-weight:700;text-transform:uppercase}
.footer-col h4+ul{margin-bottom:12px}
.footer-col ul{list-style:none}
.bottom-bar{position:absolute;top:4105px;left:0;width:1200px;height:68px;background:var(--blue-deep);color:#fff;display:flex;justify-content:center;align-items:center;gap:28px;font-size:15px}
</style>
</head>
<body>
<header class="site-header">
  <div class="brand"><i class="brand-mark"></i><span class="brand-name">Merrow Quay</span></div>
  <nav class="main-nav">
    <a class="active" href="#">HOME</a><a href="#">SERVICES</a><a href="#">FACILITIES</a><a href="#">STRATAS</a><a href="#">ABOUT US</a><a href="#">LOCAL INFORMATION</a><a href="#">CONTACT</a>
  </nav>
  <div class="search">SEARCH</div>
  <svg class="search-icon" width="24" height="24" viewBox="0 0 24 24" fill="none" stroke="#fff" stroke-width="2"><circle cx="10" cy="10" r="7"/><line x1="15" y1="15" x2="22" y2="22"/></svg>
</header>
<div class="hero" role="img" aria-label="Apartment tower beside a cable-stayed bridge at dusk"></div>
<div class="hero-stripe"></div>

<main>
  <h1 class="band">WELCOME TO MERROW QUAY</h1>
  <p class="intro">Merrow Quay is a community of 2500 residents in more than 1000 apartments, terraces and townhouses on the site of the old Harbour Refining industrial complex at the northern end of the Pyrmont Peninsula. In addition there are a number of commercial buildings housing several hundred workers. The redevelopment of the Harbour Refining site of over 11 hectares commenced in the early 1990s, and the first residents moved in during 2000. The site is now complete.</p>

  <h2 class="band">SERVICES</h2>
  <section class="grid services">
    <article class="card">
      <div class="photo"><span role="img" aria-label="Smiling woman on a phone call" style="background:linear-gradient(135deg,#e9dcc6,#b7c9cf)"></span></div>
      <h3>Building Management</h3>
      <p>Each strata makes its own building management arrangements. Some have chosen to retain Tideline Management, and some have engaged Keystone Manage. Both companies have previously managed the whole of Merrow Quay. Sailmaker Wharf and Ridge Walk Terraces have also engaged their own building managers from two separate companies. The Resident Services Manager (RSM)'s...</p>
      <a class="btn" href="#">READ MORE »</a>
    </article>
    <article class="card">
      <div class="photo"><span role="img" aria-label="Security officer speaking into a radio" style="background:linear-gradient(135deg,#dfe7ee,#4aa3d8)"></span></div>
      <h3>Security</h3>
      <p>Security officers are employed by Coastal Guard Services (CGS), the company contracted by the Community Association. CGS is an Australian company with 25 years' experience, and they take pride in the quality of the services they deliver. Their primary role is to protect the community facilities of the Merrow Quay Community Association and common...</p>
      <a class="btn" href="#">READ MORE »</a>
    </article>
    <article class="card">
      <div class="photo"><span role="img" aria-label="Three colleagues reviewing plans at a desk" style="background:linear-gradient(135deg,#d6d8dc,#3a3f4a)"></span></div>
      <h3>Strata Manager</h3>
      <p>Harlow Property Group is contracted by the Community Association to provide strata services for the Community Association and some of the individual strata plans in Merrow Quay. For further details please call 02 9000 3187 or refer to their website. Strata managers invoice the unit owners for strata levies and pay the costs incurred by...</p>
      <a class="btn" href="#">READ MORE »</a>
    </article>
    <article class="card">
      <div class="photo"><span role="img" aria-label="Cleaning staff vacuuming an office" style="background:linear-gradient(135deg,#f1f2f3,#9fb6c6)"></span></div>
      <h3>Cleaning</h3>
      <p>The Community Association and some strata plans have contracts with Brightway to provide cleaning services. Others have contracted with QuayClean. There is a notebook in each mail room where you can leave notes for your building's cleaner. If you have any other issues, contact your strata manager.</p>
      <a class="btn" href="#">READ MORE »</a>
    </article>
    <article class="card">
      <div class="photo"><span role="img" aria-label="Hands at a laptop with floating checklist documents" style="background:linear-gradient(135deg,#3c4f56,#9aa9a8)"></span></div>
      <h3>Resident Services Manager</h3>
      <p>The Resident Services Manager or RSM is located in the Estate Management office at 12 Fennick Street, on the lower ground floor of Cooperage. RSM services are available 8:00am to 4:30pm Monday to Friday. Tel: 02 9000 5522 Email: rsm@merrowquay.org.au</p>
      <a class="btn" href="#">READ MORE »</a>
    </article>
  </section>

  <h2 class="band">FACILITIES</h2>
  <section class="grid facilities">
    <article class="card">
      <div class="photo"><span role="img" aria-label="Tennis player striking a ball" style="background:linear-gradient(135deg,#1d5a5e,#0b1a2a)"></span></div>
      <h3>Tennis Courts</h3>
      <p>The Community Association owns and manages the following facilities on behalf of all residents and owners in Merrow Quay. Click on a facility to view the rules, hours of operation, etc. You can also go to the tennis courts calendar to check the availability of the courts, or email or phone the Resident Services Manager (RSM) to book a court, the Station, or the community meeting room.</p>
      <a class="btn" href="#">READ MORE »</a>
    </article>
    <article class="card">
      <div class="photo"><span role="img" aria-label="Children swimming underwater in a pool" style="background:linear-gradient(135deg,#5cc3ea,#1b7fc0)"></span></div>
      <h3>Glasshouse Pool</h3>
      <p>The Glasshouse Pool is situated next to The Station on Fennick Street. It is a glass-walled, light-filled structure with an outlook towards the Westgate Span and Tallow Bay, containing a 20 metre straight-edge heated pool marked with 5 lanes. Steps descend to change and locker rooms, with another set of steps ascending to the gym...</p>
      <a class="btn" href="#">READ MORE »</a>
    </article>
    <article class="card">
      <div class="photo"><span role="img" aria-label="Exercise bikes and gym equipment" style="background:linear-gradient(135deg,#e8e8e8,#6b6b6b)"></span></div>
      <h3>Glasshouse Gym</h3>
      <p>The Glasshouse Gym occupies an upper level within the Glasshouse extending along the eastern wall of the building and facing the Westgate Span and Tallow Bay. It is reached by ascending a flight of stairs, and is only accessible to residents. The equipment includes: 3 treadmills 1 recline bike 1 pace bike 1 stepper 1...</p>
      <a class="btn" href="#">READ MORE »</a>
    </article>
    <article class="card">
      <div class="photo"><span role="img" aria-label="Illustration of a community hall kitchen" style="background:linear-gradient(135deg,#dfe6ea,#67c6e4)"></span></div>
      <h3>The Station</h3>
      <p>The Station is the community hall at 30 Fennick Street, which is available free of charge to all Merrow Quay residents for events. It has a kitchen with a stove, microwave, fridge/freezer, sink and dishwasher. It has a maximum number of 80 people seated or 114 standing. Community Association By-laws and Rules apply to its...</p>
      <a class="btn" href="#">READ MORE »</a>
    </article>
  </section>
</main>

<footer class="site-footer">
  <div class="footer-brand"><i class="brand-mark"></i><span class="brand-name">Merrow Quay</span></div>
  <a class="social" href="#"><i></i>Social page</a>
  <div class="footer-col" style="left:405px">
    <h4>Frequent Questions</h4>
    <ul><li>Questions by topic</li><li>Deliveries</li><li>Noise complaints</li><li>Parking</li><li>Pets</li><li>Report a crime</li><li>Smoke alarm</li><li>Swipe card/FOB/air key</li><li>Tradespeople</li></ul>
  </div>
  <div class="footer-col" style="left:627px">
    <h4>Moving Procedures</h4>
    <ul><li>Moving In or Out</li></ul>
    <h4>What's On</h4>
    <ul><li>MQ What's On</li><li>Pyrmont What's On</li><li>Community Activities</li></ul>
  </div>
  <div class="footer-col" style="left:849px">
    <h4>General Info</h4>
    <ul><li>Community Management</li><li>Statement</li><li>Transport</li><li>Churches</li><li>Shops</li></ul>
  </div>
</footer>
<div class="bottom-bar"><a href="#">Privacy Policy</a><a href="#">Contact Webmaster</a><a href="#">Terms of Use</a><span>© 2023</span></div>
</body>
</html>
```